VORLA Book Cover

1. Front & back cover designs (print-ready, high resolution PDF + PNG/JPEG).
2. Spine designs consistent across the series.
3. Mockup visuals (3D renders and group images).
4. Editable source files (AI/PSD/INDD).
5. Spine- 1.3572in x 10.3in, 2138px x 3075px.
6. Front- 7.1in x 10.3in with 0.125in bleed, 2138px x 3075px. Ideal resolution 300dpi.
7. Back- 7.1in x 10.3in with 0.125in bleed, 2138px x 3075px. Ideal resolution 300dpi.

```html
<!DOCTYPE html>
<html lang="en">
<head>
<meta charset="utf-8">
<title>VORLA Book Cover</title>
<link rel="stylesheet" href="https://fonts.googleapis.com/css2?family=Oswald:wght@500&display=swap">
<style>
  :root {
    --backdrop: #293450;
    --paper: #dfe6eb;
    --navy: #243f7f;
    --sky: #4a8ade;
    --title-ink: #243f7f;
    --accent: #cfd43a;
    --portrait-light: #c9c9c9;
    --portrait-dark: #7a7a7a;
  }
  html, body {
    margin: 0;
    padding: 0;
    width: 1200px;
    height: 1001px;
    overflow: hidden;
    background: var(--backdrop);
  }
  .stage {
    position: relative;
    width: 1200px;
    height: 1001px;
  }
  .book-cover {
    position: absolute;
    left: 307px;
    top: 86px;
    width: 587px;
    height: 829px;
    display: block;
  }
  .cover-paper { fill: var(--paper); }
  .ring-outer { fill: var(--navy); }
  .ring-inner { fill: var(--paper); }
  .arc-navy { fill: var(--navy); }
  .arc-sky { fill: var(--sky); }
  .author-name, .book-title, .imprint-name {
    font-family: "Oswald", "Arial Narrow", sans-serif;
    font-weight: 500;
    fill: var(--title-ink);
  }
  .author-name { font-size: 24px; }
  .book-title { font-size: 64px; }
  .imprint-name { font-size: 46px; }
  .imprint-dot { fill: var(--accent); }
</style>
</head>
<body>
<main class="stage">
  <svg class="book-cover" viewBox="0 0 587 829" xmlns="http://www.w3.org/2000/svg">
    <defs>
      <clipPath id="cover-edge">
        <rect x="0" y="0" width="587" height="829"/>
      </clipPath>
      <linearGradient id="portrait-tone" x1="0" y1="0" x2="1" y2="1">
        <stop offset="0" stop-color="var(--portrait-light)"/>
        <stop offset="1" stop-color="var(--portrait-dark)"/>
      </linearGradient>
    </defs>

    <g clip-path="url(#cover-edge)">
      <rect class="cover-paper" x="0" y="0" width="587" height="829"/>

      <circle class="ring-outer" cx="293" cy="414" r="464"/>
      <circle class="ring-inner" cx="293" cy="414" r="371"/>

      <path class="arc-navy"
            d="M -20.8 384.8 A 320 320 0 0 0 299.2 704.8 L 299.2 668.8 A 284 284 0 0 1 15.2 384.8 Z"/>

      <path class="arc-sky"
            d="M 299.2 668.8 A 284 284 0 1 1 527.2 554.4 L 486.4 554.4 A 252.8 252.8 0 1 0 299.2 637.6 Z"/>

      <path class="author-portrait" role="img" aria-label="Author portrait photo, black and white"
            fill="url(#portrait-tone)"
            d="M 487 0 L 587 0 L 587 186 L 540 186 C 520 170 500 140 492 100 C 486 70 484 30 487 0 Z"/>
    </g>

    <text class="author-name" x="294" y="252" text-anchor="middle"
          textLength="225" lengthAdjust="spacingAndGlyphs">DAMIEN FOURCAULT PhD</text>

    <text class="book-title" x="291" y="330" text-anchor="middle"
          textLength="336" lengthAdjust="spacingAndGlyphs">HIDDEN COSTS</text>
    <text class="book-title" x="291" y="404" text-anchor="middle"
          textLength="375" lengthAdjust="spacingAndGlyphs">IN INNOVATION</text>
    <text class="book-title" x="291" y="478" text-anchor="middle"
          textLength="354" lengthAdjust="spacingAndGlyphs">LED VENTURES</text>
    <text class="book-title" x="291" y="551" text-anchor="middle"
          textLength="284" lengthAdjust="spacingAndGlyphs">EXPLAINED</text>

    <circle class="imprint-dot" cx="427" cy="632" r="12"/>
    <text class="imprint-name" x="427" y="710" text-anchor="middle"
          textLength="150" lengthAdjust="spacingAndGlyphs">VORLA</text>
  </svg>
</main>
</body>
</html>
```